Text design/overlay needed for promotional music release cover photo

I need the following text elements added to the attached image:
Element 1: Corwin Haskell and The Kinfolk Assembly
Element 2. This all needs to be clear and prominent : Featuring: Terrence Pawlak, Oscar Brandt, Danielle Oroszco, Renata Hollsworth, Marcus "Tater" Vinson, Lorraine Quibell, Wa Nu Ri Blake Dorsey, Philip Ostrander, Eddie Pruitt, Nolan Fitch, and The Final Grooveloid
Element 3 ("WINDING CREEK" needs to pop): New single WINDING CREEK available everywhere 9/26
The final image needs to be 16:9 ratio. Colors should be black and samples from the bench in the image. Various fonts, text sizes, etc. The music is a reggae/bluegrass blend. I'm looking for art not AI. Thanks!

```html
<!DOCTYPE html>
<html lang="en">
<head>
<meta charset="utf-8">
<title>Corwin Haskell &amp; The Kinfolk Assembly — Winding Creek</title>
<link rel="stylesheet" href="https://fonts.googleapis.com/css2?family=Oranienbaum&family=Montserrat:wght@500;600&family=Great+Vibes&family=EB+Garamond:ital,wght@1,600&family=Playfair+Display:wght@800&display=swap">
<style>
  :root {
    --black: #000000;
    --white: #ffffff;
    --bench-yellow: #f5e11a;
    --bench-lime: #c9dc3a;
    --leaf: #6a9e2a;
    --sky: #eef5b0;
    --gravel: #a9a590;
    --glow: #f4f000;
  }
  html, body {
    margin: 0;
    padding: 0;
    width: 1200px;
    height: 675px;
    overflow: hidden;
    background: var(--black);
  }
  .cover {
    position: relative;
    width: 1200px;
    height: 675px;
    overflow: hidden;
  }
  .cover-photo {
    position: absolute;
    inset: 0;
    background: linear-gradient(180deg, var(--sky) 0%, #9cc83a 12%, var(--leaf) 32%, #7fae34 48%, #c3c0a2 62%, var(--gravel) 82%, #7e7a68 100%);
  }
  .glow-left {
    position: absolute;
    inset: 0;
    background: linear-gradient(90deg, var(--glow) 0%, rgba(244,240,0,0.45) 5%, rgba(244,240,0,0) 16%);
  }
  .fade-right {
    position: absolute;
    inset: 0;
    background: linear-gradient(90deg, rgba(0,0,0,0) 52%, rgba(0,0,0,0.55) 60%, rgba(0,0,0,0.9) 66%, var(--black) 70%);
  }
  .frame {
    position: absolute;
    left: 29px;
    top: 29px;
    width: 1141px;
    height: 616px;
    border: 1.5px solid var(--white);
  }
  .text { position: absolute; color: var(--white); text-align: center; white-space: nowrap; margin: 0; }
  .artist {
    left: 384px; width: 440px; top: 34px;
    font-family: "Oranienbaum", serif;
    font-size: 86px; line-height: 1;
    letter-spacing: 0.06em;
    text-shadow: 0 2px 4px rgba(0,0,0,0.35);
  }
  .band {
    left: 384px; width: 440px; top: 116px;
    font-family: "Montserrat", sans-serif;
    font-weight: 500;
    font-size: 26px; line-height: 1;
    letter-spacing: 0.12em;
    text-shadow: 0 2px 4px rgba(0,0,0,0.35);
  }
  .featuring-label {
    left: 790px; width: 220px; top: 150px;
    font-family: "Great Vibes", cursive;
    font-size: 56px; line-height: 1.1;
    color: var(--bench-yellow);
  }
  .featuring-list {
    left: 650px; width: 490px; top: 212px;
    font-family: "EB Garamond", serif;
    font-style: italic; font-weight: 600;
    font-size: 21px; line-height: 27px;
    text-shadow: 0 1px 3px rgba(0,0,0,0.5);
  }
  .featuring-list span { display: block; }
  .new-single {
    left: 704px; width: 400px; top: 336px;
    font-family: "Playfair Display", serif;
    font-weight: 800;
    font-size: 36px; line-height: 1;
    letter-spacing: 0.12em;
  }
  .title-top {
    left: 690px; width: 430px; top: 378px;
    font-family: "Montserrat", sans-serif;
    font-weight: 500;
    font-size: 80px; line-height: 1;
    letter-spacing: -0.01em;
  }
  .title-bottom {
    left: 690px; width: 430px; top: 462px;
    font-family: "Montserrat", sans-serif;
    font-weight: 600;
    font-size: 112px; line-height: 1;
    color: var(--bench-lime);
  }
  .release {
    left: 704px; width: 400px; top: 580px;
    font-family: "Oranienbaum", serif;
    font-size: 28px; line-height: 1;
    letter-spacing: 0.05em;
    font-weight: 700;
  }
</style>
</head>
<body>
  <main class="cover">
    <div class="cover-photo" role="img" aria-label="Photo of a bearded musician in a cap and sunglasses relaxing on a rainbow-painted wooden bench beside a white electric guitar, on a winding gravel road through green summer hills"></div>
    <div class="glow-left"></div>
    <div class="fade-right"></div>
    <div class="frame"></div>

    <h1 class="text artist">CORWIN HASKELL &amp;</h1>
    <p class="text band">THE KINFOLK ASSEMBLY</p>

    <p class="text featuring-label">Featuring:</p>
    <p class="text featuring-list">
      <span>Terrence Pawlak, Oscar Brandt, Danielle Oroszco,</span>
      <span>Renata Hollsworth, Marcus "Tater" Vinson, Lorraine Quibell,</span>
      <span>Wa Nu Ri Blake Dorsey, Philip Ostrander,</span>
      <span>Eddie Pruitt, Nolan Fitch, and The Final Grooveloid</span>
    </p>

    <p class="text new-single">NEW SINGLE</p>
    <h2 class="text title-top">WINDING</h2>
    <p class="text title-bottom">CREEK</p>
    <p class="text release">AVAILABLE EVERYWHERE 9/26</p>
  </main>
</body>
</html>
```